Publisher seeks book cover / Book cover for publishing house

Full cover (front, back and side of the book). 28 cm x 20 cm total (High 20 cm, width 13, side 2 cm) Front cover: Title of the author on top, centered (Mathieu Lacombe) Title: Charting the skies Subtitle: Working pilot aerial Bottom and centered: attached logo (Velmora Editions) in white, and edited eventualy. Side: From left to right: Editor logo (only "Velmora" word, without the "Editions" word, title and author name Back cover: Left text column ) Bottom: space available for the bar coded price and 2 or 3 lines of text Right text column (approx 6.5 cm wide) Bottom of the right colum, center of the right column: same attached logo (Velmora Editions) in white, and edited eventualy, with www.velmora-example.com below the logo. Left Lateral margin of the back cover, this book should be almost 1 cm)
Colors
Designer to choose colors to be used in the design.
Look and feel
Each slider illustrates characteristics of the customer's brand and the style your logo design should communicate.

```html
<!DOCTYPE html>
<html lang="en">
<head>
<meta charset="utf-8">
<title>Charting the skies — full cover</title>
<link rel="stylesheet" href="https://fonts.googleapis.com/css2?family=Archivo+Black&family=Arimo:wght@400;700&family=Kalam:wght@400&display=swap">
<style>
  :root {
    --page-bg: #e9e6e1;
    --sky-top: #7f9fbc;
    --sky-mid: #a9c3d4;
    --island: #4f7668;
    --lagoon: #2eb1b6;
    --lagoon-light: #63c7c3;
    --shallows: #b4d8c8;
    --back-column: #4a6990;
    --text-light: #ffffff;
    --text-dark: #1c1c1a;
    --spine-shade: rgba(0, 0, 0, 0.12);
  }
  * { margin: 0; padding: 0; box-sizing: border-box; }
  html, body { width: 1200px; height: 800px; overflow: hidden; background: var(--page-bg); }
  .full-cover {
    position: absolute; left: 110px; top: 50px; width: 980px; height: 700px;
    box-shadow: 0 10px 30px rgba(0,0,0,0.25);
    overflow: hidden;
  }
  .cover-photo { position: absolute; inset: 0; width: 100%; height: 100%; }
  .back-cover { position: absolute; left: 0; top: 0; width: 455px; height: 700px; }
  .back-column {
    position: absolute; left: 0; top: 0; width: 245px; height: 700px;
    background: var(--back-column);
  }
  .blurb {
    font-family: "Arimo", Arial, sans-serif; font-size: 11.5px; line-height: 1.32;
    color: var(--text-light);
  }
  .blurb p + p { margin-top: 14px; }
  .blurb--left { position: absolute; left: 35px; top: 30px; width: 190px; }
  .blurb--right { position: absolute; left: 268px; top: 78px; width: 175px; }
  .price-box {
    position: absolute; left: 35px; top: 575px; width: 180px; height: 95px;
    background: #ffffff;
  }
  .publisher-mark {
    font-family: "Arimo", Arial, sans-serif; font-weight: 700; color: var(--text-dark);
    text-transform: uppercase; letter-spacing: 0.5px; text-align: center; white-space: nowrap;
  }
  .publisher-mark--back { position: absolute; left: 268px; top: 612px; width: 175px; font-size: 16px; }
  .publisher-url {
    position: absolute; left: 268px; top: 638px; width: 175px; text-align: center;
    font-family: "Arimo", Arial, sans-serif; font-size: 10px; letter-spacing: 0.5px; color: var(--text-dark);
  }
  .spine {
    position: absolute; left: 455px; top: 0; width: 70px; height: 700px;
    background: linear-gradient(90deg, var(--spine-shade), rgba(255,255,255,0.08) 50%, var(--spine-shade));
    display: flex; align-items: center; justify-content: center;
  }
  .spine-text {
    writing-mode: vertical-rl;
    display: flex; align-items: center; gap: 60px;
    height: 640px; justify-content: space-between;
    color: var(--text-light); white-space: nowrap;
  }
  .spine-publisher { font-family: "Arimo", Arial, sans-serif; font-weight: 700; font-size: 15px; text-transform: uppercase; letter-spacing: 1px; color: var(--text-dark); }
  .spine-title { font-family: "Kalam", cursive; font-size: 24px; text-transform: uppercase; letter-spacing: 2px; }
  .spine-author { font-family: "Archivo Black", Arial, sans-serif; font-size: 14px; text-transform: uppercase; letter-spacing: 1px; }
  .front-cover { position: absolute; left: 525px; top: 0; width: 455px; height: 700px; }
  .author {
    position: absolute; left: 0; top: 70px; width: 100%; text-align: center;
    font-family: "Archivo Black", Arial, sans-serif; font-size: 25px; letter-spacing: 1px;
    color: var(--text-light); text-transform: uppercase;
  }
  .title {
    position: absolute; left: 60px; top: 255px; width: 360px;
    font-family: "Kalam", cursive; font-weight: 400; color: var(--text-light);
    text-transform: uppercase; line-height: 1;
  }
  .title span { display: block; }
  .title .line-1 { font-size: 54px; letter-spacing: 3px; }
  .title .line-2 { font-size: 46px; padding-left: 110px; margin-top: 10px; }
  .title .line-3 { font-size: 62px; letter-spacing: 4px; margin-top: 6px; padding-left: 10px; }
  .subtitle {
    position: absolute; left: 0; top: 505px; width: 100%; text-align: center;
    font-family: "Arimo", Arial, sans-serif; font-size: 17px; letter-spacing: 1px;
    color: var(--text-light);
  }
  .publisher-mark--front { position: absolute; left: 0; top: 625px; width: 100%; font-size: 24px; }
</style>
</head>
<body>
  <div class="full-cover">
    <svg class="cover-photo" viewBox="0 0 980 700" preserveAspectRatio="none" role="img"
         aria-label="Aerial photograph of a small plane flying over a turquoise lagoon beside a green island under a cloudy sky">
      <defs>
        <linearGradient id="lagoon-photo" x1="0" y1="0" x2="0" y2="1">
          <stop offset="0" stop-color="var(--sky-top)"/>
          <stop offset="0.22" stop-color="var(--sky-mid)"/>
          <stop offset="0.3" stop-color="var(--island)"/>
          <stop offset="0.4" stop-color="var(--lagoon)"/>
          <stop offset="0.68" stop-color="var(--lagoon-light)"/>
          <stop offset="1" stop-color="var(--shallows)"/>
        </linearGradient>
      </defs>
      <rect width="980" height="700" fill="url(#lagoon-photo)"/>
    </svg>

    <section class="back-cover">
      <div class="back-column"></div>
      <div class="blurb blurb--left">
        <p>Lorem ipsum dolor sit amet, consectetur adipiscing elit, sed do eiusmod tempor incididunt ut labore et dolore magna aliqua. Habitant morbi tristique senectus et netus et malesuada fames ac. Aliquet porttitor lacus luctus accumsan. In est ante in nibh mauris. In hendrerit gravida rutrum quisque non tellus orci. In arcu cursus euismod quis viverra. Pretium lectus quam id leo in vitae turpis. Faucibus scelerisque eleifend donec pretium vulputate sapien nec sagittis aliquam. Nunc congue nisi vitae suscipit. Aliquam purus sit amet luctus venenatis lectus magna fringilla urna. Molestie at elementum eu facilisis sed.</p>
        <p>Dui accumsan sit amet nulla facilisi morbi tempus iaculis urna. Adipiscing bibendum est ultricies integer quis auctor elit sed vulputate. Bibendum neque egestas congue purus faucibus ornare suspendisse sed.</p>
      </div>
      <div class="price-box"></div>
      <div class="blurb blurb--right">
        <p>Lorem ipsum dolor sit amet, consectetur adipiscing elit, sed do eiusmod tempor incididunt ut labore et dolore magna aliqua. Habitant morbi tristique senectus et netus et malesuada fames ac. Aliquet porttitor lacus luctus accumsan. In est ante in nibh mauris. In hendrerit gravida rutrum quisque non tellus orci. Pretium lectus quam id leo in vitae turpis. Faucibus scelerisque eleifend donec pretium vulputate sapien nec sagittis aliquam. Molestie at elementum eu facilisis sed.</p>
        <p>Dui accumsan sit amet nulla facilisi morbi tempus iaculis urna. Adipiscing bibendum est ultricies integer quis auctor elit sed vulputate. Enim diam vulputate ut pharetra sit amet. Tortor vitae purus faucibus ornare suspendisse sed.</p>
        <p>Enim diam vulputate. Mauris nunc congue nisi vitae suscipit tellus mauris a diam.</p>
      </div>
      <div class="publisher-mark publisher-mark--back">Velmora Editions</div>
      <div class="publisher-url">www.velmora-example.com</div>
    </section>

    <div class="spine">
      <div class="spine-text">
        <span class="spine-publisher">Velmora</span>
        <span class="spine-title">Charting the skies</span>
        <span class="spine-author">Mathieu Lacombe</span>
      </div>
    </div>

    <section class="front-cover">
      <div class="author">Mathieu Lacombe</div>
      <h1 class="title">
        <span class="line-1">Charting</span>
        <span class="line-2">the</span>
        <span class="line-3">skies</span>
      </h1>
      <p class="subtitle">Working pilot aerial</p>
      <div class="publisher-mark publisher-mark--front">Velmora Editions</div>
    </section>
  </div>
</body>
</html>
```